Ashworth Web Design Project

I need the front page and an internal page designed for this client's website. The logo is attached. Obviously the colors have to go with and/or work with the logo colors. I also attached a very rough brochure layout to help you see the direction we're going in with print materials. The rough site map is also attached. I see a slider on the homepage, the art for which I may come back to you to create. This clinic is in a very high end Dallas neighborhood. The hook is that it's a primary care and urgent facility with convenient hours.

I don't know how much this impacts your design, but this will be a Wordpress site and I'm using a framework called Struxo (struxo-demo.example). If Struxo proves to be inflexible, I'll have to get a template that allows me to execute your design.

This site (http://oakbendcareclinic.example) has the type and quality of content I will eventually have on the Ashworth site.

I just revised the brief for this project. I added the site map and added details to the overview and the "Must Have" section. Thank you for revisiting the brief. 

Reason: Christmas was a bad time to end it.

Target Market(s)

Women 25-54 with children living at home, income over $150k/year

Industry/Entity Type

Clinic

Requirements
Must have
• Masthead incorporating the logo
Followed by the primary nav
Slider on the home page below that
Dual nav - 1 with the nav in the attached site map
2 secondary nav with areas of healthcare
There will three blocks under the nav
1. It's about time (with a small blurb less than 50 words.
2. It's about choices (with small blurb)
3. It's about you (with small blurb)
Three footer blocks
patient check in link on every page
"No appointment? No problem" icon on every page

```html
<!DOCTYPE html>
<html lang="en">
<head>
<meta charset="utf-8">
<title>Ashworth Medical – Immediate Family and Personal Care</title>
<link href="https://fonts.googleapis.com/css2?family=Arimo:wght@400;700&display=swap" rel="stylesheet">
<style>
:root{
  --blue:#0f4e8c;
  --blue-dark:#0b3f73;
  --green:#12a04a;
  --text:#444;
  --heading:#555;
  --rule:#d9d9d9;
  --footer-bg:#555;
  --footer-link:#dcdcdc;
  --white:#fff;
}
*{margin:0;padding:0;box-sizing:border-box}
html,body{width:1200px;height:1200px;overflow:hidden;background:var(--white)}
body{position:relative;font-family:"Arimo",Arial,sans-serif;color:var(--text)}
a{text-decoration:none;color:inherit}

.brand{position:absolute;left:120px;top:16px;display:flex;align-items:center;gap:10px}
.brand-mark{width:54px;height:54px;border-radius:50%;background:var(--blue)}
.brand-name{font-size:33px;font-weight:700;color:var(--blue);letter-spacing:-.5px;line-height:1}
.brand-tag{font-size:11px;color:#444;margin-top:4px;text-align:center;font-weight:700}

.utility{position:absolute;right:120px;top:11px;font-size:11px;color:var(--blue);display:flex;gap:12px}
.utility .sep{color:#333}
.social{position:absolute;top:43px;right:120px;display:flex;gap:8px}
.social span{width:32px;height:32px;border-radius:4px;display:block}
.social .s1{background:#3b5d9c}.social .s2{background:#4fc1e9}.social .s3{background:#c4302b}

.mainnav{position:absolute;left:119px;top:106px;width:962px;height:46px;border:1px solid #e0e0e0;
  background:linear-gradient(#fff 0%,#fbfbfb 55%,#eeeeee 56%,#f6f6f6 100%);display:flex;font-size:12px;color:#444}
.mainnav .item{height:100%;display:flex;align-items:center;padding:0 21px;border-right:1px solid #ddd}
.mainnav .home{width:60px;justify-content:center;padding:0}
.noappt{position:absolute;left:780px;top:0;height:100%;display:flex;align-items:center;gap:10px;font-weight:700;color:#333}

.slider{position:absolute;left:120px;top:163px;width:959px;height:390px;
  background:linear-gradient(90deg,#8fb86a 0%,#c9de9c 30%,#cde3a2 60%,#a9c77a 80%,#7fa45a 100%);box-shadow:0 0 3px #bbb}
.slide-card{position:absolute;left:339px;top:267px;width:336px;height:101px;background:var(--white);border:2px solid #e4e4e4;box-shadow:0 0 4px rgba(0,0,0,.2);
  display:flex;align-items:center;justify-content:center;gap:10px}
.slide-card .brand-mark{width:42px;height:42px}
.slide-card .brand-name{font-size:27px}
.slide-card .brand-tag{font-size:9px}
.dots{position:absolute;right:19px;bottom:17px;display:flex;gap:4px}
.dots i{width:14px;height:14px;border-radius:50%;background:var(--blue);border:2px solid #fff}
.dots i.on{background:var(--green)}

.blocks{position:absolute;top:578px;left:120px;width:961px}
.block{position:absolute;top:0;width:296px}
.block h2{font-size:24px;color:var(--heading);padding-bottom:6px;border-bottom:1px solid var(--rule);margin-bottom:5px}
.block p{font-size:12.4px;line-height:20px}
.more{font-size:12px;font-weight:700;color:var(--green);line-height:20px}

.carenav{position:absolute;left:119px;top:754px;width:223px;list-style:none}
.carenav li{height:30px;border-bottom:1px solid var(--rule);display:flex;align-items:center;justify-content:space-between;
  font-size:12px;font-weight:700;color:var(--blue)}
.carenav li::after{content:"";border-left:6px solid var(--green);border-top:5px solid transparent;border-bottom:5px solid transparent;margin-right:0}

.welcome{position:absolute;left:453px;top:754px;width:625px}
.welcome h1{font-size:24px;color:var(--heading)}
.welcome h1 .b{color:var(--blue)}.welcome h1 .g{color:var(--green)}
.welcome p{font-size:12px;line-height:20px;margin:14px 0 0 4px;color:#555}
.welcome p+p{margin-top:20px}

.footer{position:absolute;left:0;top:1008px;width:1200px;height:192px;background:var(--footer-bg)}
.footcol{position:absolute;top:36px;list-style:none;font-size:11px;color:var(--footer-link)}
.footcol li{height:28px}
.foot-brand{position:absolute;left:912px;top:40px;width:169px;height:52px;background:var(--white);border:2px solid #e6e6e6;
  display:flex;align-items:center;justify-content:center;gap:5px}
.foot-brand .brand-mark{width:20px;height:20px}
.foot-brand .brand-name{font-size:14px}
.copy{position:absolute;right:119px;top:150px;font-size:11px;color:var(--footer-link)}
</style>
</head>
<body>

<header>
  <div class="brand">
    <span class="brand-mark"></span>
    <div><div class="brand-name">Ashworth Medical</div><div class="brand-tag">Immediate Family and Personal Care</div></div>
  </div>
  <nav class="utility"><a href="#">Register</a><span class="sep">|</span><a href="#">Login</a><span class="sep">|</span><a href="#">Blog</a><span class="sep">|</span><a href="#">Patient check in</a></nav>
  <div class="social"><span class="s1"></span><span class="s2"></span><span class="s3"></span></div>
</header>

<nav class="mainnav">
  <a class="item home" href="#" aria-label="Home"><svg width="24" height="22" viewBox="0 0 24 22"><path d="M2 11 12 2l10 9" fill="none" stroke="#777" stroke-width="2"/><path d="M5 10v11h5v-6h4v6h5V10" fill="#ddd" stroke="#777" stroke-width="1.5"/></svg></a>
  <a class="item" href="#">About</a><a class="item" href="#">Services</a><a class="item" href="#">Staff</a>
  <a class="item" href="#">Insurance</a><a class="item" href="#">Videos</a><a class="item" href="#">Contact Us</a>
  <div class="noappt"><svg width="28" height="30" viewBox="0 0 28 30"><circle cx="13" cy="16" r="10" fill="#eee" stroke="#888" stroke-width="2"/><path d="M13 10v6h4" stroke="#666" stroke-width="2" fill="none"/><path d="M20 22l5 7h-10z" fill="#f29b1d"/></svg>No Appointment</div>
</nav>

<section class="slider" role="img" aria-label="Smiling families outdoors in a sunny green field">
  <div class="slide-card">
    <span class="brand-mark"></span>
    <div><div class="brand-name">Ashworth Medical</div><div class="brand-tag">Immediate Family and Personal Care</div></div>
  </div>
  <div class="dots"><i class="on"></i><i></i><i></i><i></i></div>
</section>

<section class="blocks">
  <article class="block" style="left:0"><h2>Heading 1</h2><p>Lorem ipsum dolor sit amet consecutor. Lorem ipsum dolor sit amet consecutor. Lorem ipsum dolor sit amet consecutor. Lorem ipsum dolor sit amet consecutor. Lorem ipsum dolor sit amet consecutor.</p><a class="more" href="#">Read More...</a></article>
  <article class="block" style="left:331px"><h2>Heading 2</h2><p>Lorem ipsum dolor sit amet consecutor. Lorem ipsum dolor sit amet consecutor. Lorem ipsum dolor sit amet consecutor. Lorem ipsum dolor sit amet consecutor. Lorem ipsum dolor sit amet consecutor.</p><a class="more" href="#">Read More...</a></article>
  <article class="block" style="left:664px"><h2>Heading 3</h2><p>Lorem ipsum dolor sit amet consecutor. Lorem ipsum dolor sit amet consecutor. Lorem ipsum dolor sit amet consecutor. Lorem ipsum dolor sit amet consecutor. Lorem ipsum dolor sit amet consecutor.</p><a class="more" href="#">Read More...</a></article>
</section>

<ul class="carenav">
  <li>Immediate Care</li><li>Allergies</li><li>Primary Care</li><li>Women’s Health</li>
  <li>Medical Spa Treatments</li><li>Men’s Health</li><li>Weight Loss</li>
</ul>

<section class="welcome">
  <h1>Welcome to the <span class="b">Ashworth</span> <span class="g">Medical</span></h1>
  <p>Lorem ipsum dolor sit amet consecutor. Lorem ipsum dolor sit amet consecutor. Lorem ipsum dolor sit amet consecutor. Lorem ipsum dolor sit amet consecutor. Lorem ipsum dolor sit amet consecutor. Lorem ipsum dolor sit amet consecutor. Lorem ipsum dolor sit amet consecutor. Lorem ipsum dolor sit amet consecutor. Lorem ipsum dolor sit amet consecutor. Lorem ipsum dolor sit amet consecutor. Lorem ipsum dolor sit amet consecutor.</p>
  <p>Lorem ipsum dolor sit amet consecutor. Lorem ipsum dolor sit amet consecutor. Lorem ipsum dolor sit amet consecutor. Lorem ipsum dolor sit amet consecutor. Lorem ipsum dolor sit amet consecutor. Lorem ipsum dolor sit amet consecutor. Lorem ipsum dolor sit amet consecutor. Lorem ipsum dolor sit amet consecutor. Lorem</p>
</section>

<footer class="footer">
  <ul class="footcol" style="left:122px"><li>Dummy Link 1</li><li>Dummy Link 2</li><li>Dummy Link 3</li><li>Dummy Link 4</li><li>Dummy Link 5</li></ul>
  <ul class="footcol" style="left:393px"><li>Dummy Link 1</li><li>Dummy Link 2</li><li>Dummy Link 3</li><li>Dummy Link 4</li><li>Dummy Link 5</li></ul>
  <ul class="footcol" style="left:654px"><li>Dummy Link 1</li><li>Dummy Link 2</li><li>Dummy Link 3</li><li>Dummy Link 4</li><li>Dummy Link 5</li></ul>
  <div class="foot-brand"><span class="brand-mark"></span><span class="brand-name">Ashworth Medical</span></div>
  <p class="copy">Copyright © 2012 Ashworth Medical</p>
</footer>

</body>
</html>
```